Business Card Design Project

I need a business card design for our new logo, please check the logo at the following link:
https://www.filecrate.net/s/q7rtx2pw9kd41m/FernLoop.png
The address on the business card:
Av. Gervásio Tavares 418 sala 207
Barra da Tijuca, Rio de Janeiro, RJ
CEP: 22714-380
Brasil
Phone: +55 21 86347215
e-mail: osvaldo@fernloop.com.br
Updates
Thank you all for sending your designs, we will not provide feedback because there are too many designs, on December 3 we will pick the best design according to our point of view. Please keep posting.
Osvaldo
Industry/Entity Type
Business
Look and feel
Each slider illustrates characteristics of the customer's brand and the style your logo design should communicate.

```html
<!DOCTYPE html>
<html lang="pt-BR">
<head>
<meta charset="utf-8">
<title>FernLoop – Business Card</title>
<link rel="stylesheet" href="https://fonts.googleapis.com/css2?family=Noto+Sans:wght@400;700&display=swap">
<style>
  :root {
    --rust-deep: #5e2c20;
    --rust-mid: #8a4535;
    --rust-light: #9c5443;
    --hazard-orange: #d9780f;
    --ink: #1e1e1e;
    --paper: #f4f1f3;
  }
  html, body {
    margin: 0;
    padding: 0;
    width: 1200px;
    height: 617px;
    overflow: hidden;
    background: #ffffff;
  }
  .card {
    position: relative;
    width: 1200px;
    height: 617px;
    overflow: hidden;
    font-family: "Noto Sans", Verdana, sans-serif;
  }
  .card__texture {
    position: absolute;
    inset: 0;
    background:
      radial-gradient(ellipse at 30% 40%, var(--rust-light) 0%, transparent 60%),
      radial-gradient(ellipse at 85% 30%, var(--rust-deep) 0%, transparent 55%),
      linear-gradient(135deg, var(--rust-mid) 0%, var(--rust-deep) 100%);
  }
  .card__hazard-band {
    position: absolute;
    left: 0;
    top: 458px;
    width: 1200px;
    height: 66px;
    background: linear-gradient(90deg, rgba(217,120,15,0.55), rgba(217,120,15,0.75) 50%, rgba(217,120,15,0.55));
  }
  .brand-name {
    position: absolute;
    left: 30px;
    top: 282px;
    margin: 0;
    font-size: 128px;
    font-weight: 700;
    line-height: 1;
    letter-spacing: -2px;
    color: var(--ink);
  }
  .address {
    position: absolute;
    left: 598px;
    top: 80px;
    margin: 0;
    font-style: normal;
    font-size: 22px;
    line-height: 26px;
    color: var(--paper);
  }
  .contact {
    position: absolute;
    left: 598px;
    top: 545px;
    margin: 0;
    font-size: 22px;
    line-height: 29px;
    color: var(--paper);
  }
  .contact p, .address p { margin: 0; }
</style>
</head>
<body>
  <main class="card">
    <div class="card__texture" role="img" aria-label="Weathered rusty metal surface texture"></div>
    <div class="card__hazard-band" role="img" aria-label="Band of diagonal orange hazard stripes"></div>

    <h1 class="brand-name">FernLoop</h1>

    <address class="address">
      <p>Av. Gervásio Tavares 418 sala 207</p>
      <p>Barra da Tijuca, Rio de Janeiro, RJ</p>
      <p>CEP: 22714-380</p>
      <p>Brasil</p>
    </address>

    <div class="contact">
      <p>Phone: +55 21 86347215</p>
      <p>e-mail: osvaldo@fernloop.com.br</p>
    </div>
  </main>
</body>
</html>
```